Poster for the 'LFA Monthly Draw'

We are a parents association for a senior school and have a number of money raising activities.

We require a poster a lucky draw where parents who subscribe £20 for the school year are entered into a monthly cash prize draw.

Draws are performed monthly. Some detail about it is available here

http://www.larchfield.example-school.uk/lfa/what-is-350-circle

We are changing the name from 'The 350 circle' to 'LFA Monthly draw', although we don't need the name change highlighted or noted on the poster

A logo is available on the word document application at the above link. Not sure of the quality. I can look to obtain a better resolution, but no promises.

A brief overview of the LFA can be read here for any thoughts / inspiration.

We don't want any reference to specific items purchased, unless we can easily update this on the poster ourselves.

http://www.larchfield.example-school.uk/lfa

Target Market(s)

Parents of school kids aged 13 to 17 from whom we are trying to raise contributions to so as to provide funding to school departments who have need to additional items that are not available via the school budget.

Industry/Entity Type

School

Requirements
Must have
• LFA Parents association logo, as in the current 350 circle application, should appear.
• Reference to the amount to be contributed of £20 for the year.
• Reference to the monthly prize draw amounts of
• 1st prize - £30
• 2nd prize - £20
• 3rd Prize £10
• Please note all spellings are to be UK english, not American english.
• Payment methods should be highlighted being
• - Trenvolo- via the school website
• - Cash
• - Cheque - Payable to Larchfield’s Parents’ Association 350 Circle
• No specific colour scheme, although you will see from the school website what the colours are and this should have some representation, but not overbearing.
• The following text is to appear
• The LFA Monthly Draw is a fundraiser for the Larchfield Parent Association. We raise funds to provide the best possible resources and facilities, for your children, to enhance their learning.
• Thank you for your support of the LFA
Nice to have
• The font type is not to critical, however, it should be easy to read in a short space of time as people are walking past, so not excessive amounts of text detail and not to small a font.

```html
<!DOCTYPE html>
<html lang="en-GB">
<head>
<meta charset="utf-8">
<title>LFA Monthly Draw</title>
<link rel="stylesheet" href="https://fonts.googleapis.com/css2?family=Archivo+Black&family=Montserrat:ital,wght@0,300;0,400;0,600;0,800;1,800&display=swap">
<style>
  :root {
    --crimson: #b3214c;
    --crimson-light: #c22c58;
    --crimson-dark: #8e1638;
    --band-text: #a51c45;
    --white: #ffffff;
  }
  * { box-sizing: border-box; margin: 0; padding: 0; }
  html, body { width: 832px; height: 1200px; overflow: hidden; background: var(--crimson); }
  .poster {
    position: relative;
    width: 832px;
    height: 1200px;
    overflow: hidden;
    font-family: "Montserrat", sans-serif;
    color: var(--white);
  }
  .backdrop {
    position: absolute; inset: 0;
    background: radial-gradient(ellipse at 40% 30%, var(--crimson-light) 0%, var(--crimson) 55%, #a81d46 100%);
  }
  .shapes { position: absolute; inset: 0; }

  .masthead {
    position: absolute;
    left: 290px; top: 112px;
    width: 560px;
    transform: rotate(-15deg);
    transform-origin: 0 100%;
  }
  .masthead-row { display: flex; align-items: flex-end; }
  .masthead-initials {
    font-weight: 800;
    font-size: 156px;
    line-height: 0.8;
    letter-spacing: -2px;
  }
  .masthead-name {
    font-weight: 400;
    font-size: 18px;
    line-height: 1.05;
    margin: 0 0 56px 8px;
  }
  .masthead-title {
    font-weight: 300;
    font-size: 38px;
    letter-spacing: 1px;
    margin: 10px 0 0 110px;
    line-height: 1;
  }

  .offer {
    position: absolute;
    left: 210px; top: 368px;
    transform: rotate(-15deg);
    transform-origin: 0 0;
    font-family: "Archivo Black", sans-serif;
    font-size: 27px;
    line-height: 34px;
    color: var(--band-text);
    white-space: nowrap;
  }

  .info { position: absolute; left: 50px; top: 496px; width: 620px; }
  .info-block { position: relative; padding-left: 45px; margin-bottom: 32px; }
  .info-block::before {
    content: "";
    position: absolute; left: 0; top: 5px;
    border-left: 20px solid var(--white);
    border-top: 12px solid transparent;
    border-bottom: 12px solid transparent;
  }
  .info-heading {
    font-weight: 800; font-style: italic;
    font-size: 26px; line-height: 30px;
  }
  .info-text { font-size: 19px; line-height: 24.5px; font-weight: 400; }
  .prize-list { list-style: none; font-family: "Archivo Black", sans-serif; font-size: 19px; line-height: 24.5px; }
  .payment-list { list-style: none; }
  .payment-method { font-family: "Archivo Black", sans-serif; }

  .thanks {
    position: absolute;
    left: 362px; top: 1058px;
    transform: rotate(-17deg);
    transform-origin: 0 0;
    font-size: 25px; font-weight: 400;
    white-space: nowrap;
  }

  .association-mark {
    position: absolute;
    left: 630px; top: 1022px;
    width: 170px;
    display: flex; flex-direction: column; align-items: center;
    text-align: center;
  }
  .association-dot {
    width: 70px; height: 70px; border-radius: 50%;
    background: var(--white);
    margin-bottom: 10px;
  }
  .association-name { font-weight: 600; font-size: 17px; line-height: 21px; }
</style>
</head>
<body>
<main class="poster">
  <div class="backdrop" role="img" aria-label="Soft crimson diamond pattern background"></div>

  <svg class="shapes" width="832" height="1200" viewBox="0 0 832 1200" aria-hidden="true">
    <polygon points="0,70 270,44 262,88 0,112" fill="var(--crimson-dark)" opacity="0.45"/>
    <polygon points="232,60 270,44 205,300 170,300" fill="var(--crimson-dark)" opacity="0.45"/>
    <polygon points="400,262 832,146 832,158 403,274" fill="var(--white)"/>
    <polygon points="200,352 832,182 832,266 200,436" fill="var(--white)"/>
    <polygon points="345,1036 832,906 832,924 350,1052" fill="var(--white)" opacity="0.22"/>
  </svg>

  <header class="masthead">
    <div class="masthead-row">
      <span class="masthead-initials">LFA</span>
      <span class="masthead-name">The<br>Larchfield<br>Parents’<br>Association</span>
    </div>
    <h1 class="masthead-title">MONTHLY DRAW</h1>
  </header>

  <p class="offer">Suscribe £20 for the school year<br>and enter a monthly cash prize draw!</p>

  <section class="info">
    <div class="info-block">
      <h2 class="info-heading">WHO</h2>
      <p class="info-text">The LFA Monthly Draw is a fundraiser for the Larchfield Parent Association. We raise funds to provide the best possible resources and facilities, for your children, to enhance their learning.</p>
    </div>
    <div class="info-block">
      <h2 class="info-heading">WHAT</h2>
      <p class="info-text">Your chance to win cash prizes for just £20!</p>
      <ul class="prize-list">
        <li>1st prize - £30</li>
        <li>2nd prize - £20</li>
        <li>3rd Prize £10</li>
      </ul>
    </div>
    <div class="info-block">
      <h2 class="info-heading">HOW</h2>
      <p class="info-text">Payment can be made via</p>
      <ul class="payment-list info-text">
        <li>- <span class="payment-method">Trenvolo</span> (via the school website)</li>
        <li>- <span class="payment-method">Cash</span></li>
        <li>- <span class="payment-method">Cheque</span> (Payable to Larchfield’s Parents’ Association 350 Circle)</li>
      </ul>
    </div>
  </section>

  <p class="thanks">Thank you for your support of the LFA!</p>

  <div class="association-mark">
    <span class="association-dot"></span>
    <span class="association-name">Larchfield School Parents’ Association</span>
  </div>
</main>
</body>
</html>
```